依頼詳細
ロゴのみ支給(ロゴは黒でも白でもグレーでも明度にこだわりないです)
片面モノクロ印刷、91×55mm、縦横どちらでも可。
シンプル×スタイリッシュ×女性的な感じでお願いします。
記載項目
役職・氏名・フリガナ英字
英字店名・フリガナカタカナ
住所・電話番号
※順不同OK
字が小さすぎないほうがいいです。
希望イメージ
シンプル 複雑
単色 カラフル
暗い 明るい
日常 高級
遊び心 厳粛
未来的 伝統的
女性的 男性的
希望する色
無彩色系
納品ファイル
• イラストレーター形式 (.ai)
• フォトショップ形式 (.psd)
補足説明
ロゴデータ開けないとのことでしたので追加いたします!
■ 選んだ理由

ロゴのバックデザインが気に入りました!

■ 提案者全員のお礼・コメント

この度はご提案いただきありがとうございました!とても迷いましたが様々なデザインがみれて楽しかったです!また機会がありましたらどうぞよろしくお願いいたします。

```html
<!DOCTYPE html>
<html lang="ja">
<head>
<meta charset="utf-8">
<title>lue by solenne — stylist card</title>
<link href="https://fonts.googleapis.com/css2?family=Noto+Sans+JP:wght@400;500;700&display=swap" rel="stylesheet">
<style>
  :root {
    --card-grey: #6b6b6b;
    --ink-white: #ffffff;
  }
  html, body {
    margin: 0;
    padding: 0;
    overflow: hidden;
    background: var(--card-grey);
  }
  .card {
    position: relative;
    width: 726px;
    height: 1200px;
    background: var(--card-grey);
    color: var(--ink-white);
    font-family: "Noto Sans JP", sans-serif;
    overflow: hidden;
  }
  .card-frame {
    position: absolute;
    left: 19px;
    top: 19px;
    width: 680px;
    height: 1154px;
    border: 4px solid var(--ink-white);
  }
  .shop-name {
    position: absolute;
    left: 0;
    width: 100%;
    text-align: center;
    font-family: "Noto Sans JP", sans-serif;
    font-weight: 500;
    margin: 0;
    line-height: 1;
  }
  .shop-name__main {
    top: 150px;
    font-size: 120px;
    letter-spacing: 6px;
  }
  .shop-name__sub {
    top: 300px;
    font-size: 32px;
    letter-spacing: 1px;
  }
  .divider {
    position: absolute;
    left: 333px;
    top: 362px;
  }
  .role {
    position: absolute;
    left: 0;
    width: 100%;
    top: 548px;
    text-align: center;
    font-weight: 700;
    font-size: 34px;
    margin: 0;
    line-height: 1;
  }
  .name {
    position: absolute;
    top: 620px;
    left: 0;
    width: 100%;
    display: flex;
    justify-content: center;
    gap: 44px;
  }
  .name__part {
    display: flex;
    flex-direction: column;
    align-items: center;
  }
  .name__kanji {
    font-size: 46px;
    font-weight: 500;
    line-height: 1;
    letter-spacing: 2px;
  }
  .name__roman {
    font-size: 22px;
    font-weight: 700;
    line-height: 1;
    margin-top: 12px;
  }
  .contact__row {
    position: absolute;
    display: flex;
    align-items: center;
    height: 50px;
    font-size: 38px;
    line-height: 1;
  }
  .contact__row--postal { left: 213px; top: 846px; }
  .contact__row--address { left: 230px; top: 902px; letter-spacing: 1px; font-size: 40px; }
  .contact__row--phone { left: 172px; top: 967px; }
  .contact__icon {
    width: 44px;
    height: 44px;
    margin-right: 18px;
    flex: none;
  }
</style>
</head>
<body>
  <div class="card">
    <div class="card-frame"></div>

    <p class="shop-name shop-name__main">lue</p>
    <p class="shop-name shop-name__sub">by solenne</p>

    <svg class="divider" width="60" height="170" viewBox="0 0 60 170" fill="none" stroke="#ffffff" stroke-width="3" stroke-linecap="round">
      <circle cx="12" cy="12" r="8"/>
      <circle cx="48" cy="12" r="8"/>
      <line x1="18" y1="18" x2="42" y2="52"/>
      <line x1="42" y1="18" x2="18" y2="52"/>
      <line x1="30" y1="68" x2="30" y2="90"/>
      <line x1="30" y1="102" x2="30" y2="124"/>
      <line x1="30" y1="136" x2="30" y2="158"/>
    </svg>

    <p class="role">stylist</p>

    <div class="name">
      <div class="name__part">
        <span class="name__kanji">佐藤</span>
        <span class="name__roman">sato</span>
      </div>
      <div class="name__part">
        <span class="name__kanji">彩</span>
        <span class="name__roman">aya</span>
      </div>
    </div>

    <div class="contact__row contact__row--postal">
      <svg class="contact__icon" viewBox="0 0 44 44" aria-hidden="true">
        <circle cx="22" cy="22" r="21" fill="#ffffff"/>
        <g stroke="#6b6b6b" stroke-width="3" stroke-linecap="round">
          <line x1="13" y1="13" x2="31" y2="13"/>
          <line x1="13" y1="20" x2="31" y2="20"/>
          <line x1="22" y1="20" x2="22" y2="33"/>
        </g>
      </svg>
      <span>000-0000</span>
    </div>
    <div class="contact__row contact__row--address">
      <span>□□□□□□□</span>
    </div>
    <div class="contact__row contact__row--phone">
      <svg class="contact__icon" viewBox="0 0 44 44" aria-hidden="true">
        <circle cx="22" cy="22" r="21" fill="#ffffff"/>
        <path d="M15 12c1.5-1 3-1 3.8.4l2 3.4c.6 1 .3 2.2-.6 2.9l-1.4 1c.9 2.3 2.5 4 4.8 5l1-1.4c.7-.9 1.9-1.2 2.9-.6l3.4 2c1.4.8 1.4 2.3.4 3.8-1.2 1.8-3.3 2.5-5.3 1.8-5.4-1.9-9.4-5.9-11.3-11.3-.7-2 0-4.1 1.8-5.3z" fill="#6b6b6b"/>
      </svg>
      <span>0000-00-0000</span>
    </div>
  </div>
</body>
</html>
```